hello! I need a very simple modern business card for a new venture called The Quiet Harbour Asia. It's the very first Tech-Free retreat in Asia!

The concept is very unique. Basically a group of 12-15 people would go on a 3 to 4 days retreat where no phone or internet is allowed. The first retreat will take place in a beautiful villa in Bali by the sea. It will include yoga, meditation, art & writing workshops, swimming, hiking, cooking, healthy vegetarian meals, etc.

Reason: Thanks for your submissions. I still haven't found exactly what I'm after but the designs that haven't be eliminated are getting close.. Please keep in mind that it should be a simple, modern and upmarket business card. Thanks

Target Market(s)

Both men and women who would like to disconnect from life, computer and phone for 3/4 days. They can be either local or expats but based in Asia (Singapore, Hong Kong).
Client will have to pay for their own flight and then the price is around US$600 for a 3-day retreat including everything (accommodation, food, activities). It means clients already have a good income. They are usually working in marketing, advertising, digital media, public relations.

Industry/Entity Type

Internet

Font styles to use
Other font styles liked:
• anything modern you like

Colors
acd036
9bcb3c
f37022
f68d4d
1b1b1b
333333
acd037

Requirements
Must have
• Name: Rel Vontaine
Position: #screenwanderer
Company: The Quiet Harbour Asia (asia should be smaller than the rest)
- Email button - quietharbourasia@mailnest.example
- Facepage button - www.facepage.example/quietharbourasia
- Ticketloom button - www.quietharbourasia.ticketloom.example
Nice to have
• You can use my logo attached but it's something I designed quickly on Power Point so it would be nice to include your own version.
Should not have
• anything tacky or girly or childish. thanks

```html
<!DOCTYPE html>
<html lang="en">
<head>
<meta charset="utf-8">
<title>The Quiet Harbour Asia – Business Card</title>
<link rel="stylesheet" href="https://fonts.googleapis.com/css2?family=Montserrat:wght@300;400;500&display=swap">
<style>
  :root {
    --orange: #f37022;
    --orange-light: #f68d4d;
    --orange-shade: #8a3b12;
    --brown-slot: #5e3324;
    --green: #9bcb3c;
    --ink: #333333;
    --ink-dark: #1b1b1b;
    --paper: #ffffff;
    --backdrop: #e9ebec;
  }
  * { box-sizing: border-box; margin: 0; padding: 0; }
  html, body {
    width: 1200px; height: 1000px; overflow: hidden;
    background: var(--backdrop);
    font-family: "Montserrat", sans-serif;
  }
  .card {
    position: absolute;
    left: 240px;
    width: 720px; height: 416px;
    box-shadow: 0 6px 18px rgba(0,0,0,.15);
  }
  .card--front {
    top: 50px;
    background: linear-gradient(90deg, var(--orange-shade) 0%, #c4541b 14%, var(--orange) 30%, var(--orange) 100%);
  }
  .card--back { top: 522px; background: var(--paper); }

  .mark-dot {
    position: absolute; left: 236px; top: 64px;
    width: 112px; height: 112px; border-radius: 50%;
    background: var(--brown-slot);
  }

  .wordmark {
    position: absolute;
    font-weight: 500;
    line-height: 1;
    letter-spacing: .02em;
  }
  .wordmark span { display: block; }
  .wordmark__the { font-size: 30px; }
  .wordmark__main { font-size: 38px; text-transform: uppercase; margin-top: 2px; }
  .wordmark__asia { font-size: 26px; margin-top: 4px; }

  .card--front .wordmark { left: 438px; top: 218px; color: var(--paper); }
  .card--front .wordmark__asia { padding-left: 140px; }

  .card--back .wordmark { left: 70px; top: 46px; color: var(--orange); }
  .card--back .wordmark__asia { padding-left: 140px; }

  .person {
    position: absolute; right: 64px; top: 128px; text-align: right;
  }
  .person__name {
    font-size: 22px; font-weight: 500; color: var(--orange);
    font-variant: small-caps; letter-spacing: .06em;
  }
  .person__role { font-size: 18px; font-weight: 300; color: var(--ink); margin-top: 4px; }

  .contacts {
    position: absolute; right: 60px; top: 244px;
    list-style: none;
  }
  .contacts__item {
    display: flex; align-items: center; justify-content: flex-end;
    gap: 10px; height: 36px;
    font-size: 18px; font-weight: 300; color: var(--ink);
  }
  .contacts__icon { width: 27px; height: 27px; flex: none; display: block; }
  .contacts__square { width: 27px; height: 27px; flex: none; border-radius: 3px; }
  .contacts__square--page { background: var(--ink); }
  .contacts__square--tickets { background: var(--orange); }
</style>
</head>
<body>

<section class="card card--front" aria-label="Card front">
  <div class="mark-dot"></div>
  <div class="wordmark">
    <span class="wordmark__the">The</span>
    <span class="wordmark__main">Quiet</span>
    <span class="wordmark__main">Harbour</span>
    <span class="wordmark__asia">Asia</span>
  </div>
</section>

<section class="card card--back" aria-label="Card back">
  <div class="wordmark">
    <span class="wordmark__the">The</span>
    <span class="wordmark__main">Quiet</span>
    <span class="wordmark__main">Harbour</span>
    <span class="wordmark__asia">Asia</span>
  </div>

  <div class="person">
    <p class="person__name">Rel Vontaine</p>
    <p class="person__role">#screenwanderer</p>
  </div>

  <ul class="contacts">
    <li class="contacts__item">
      <span>quietharbourasia@mailnest.example</span>
      <svg class="contacts__icon" viewBox="0 0 27 27" aria-hidden="true">
        <rect width="27" height="27" rx="3" fill="var(--green)"/>
        <rect x="5" y="8" width="17" height="12" fill="#fff"/>
        <polyline points="5,8 13.5,15 22,8" fill="none" stroke="var(--green)" stroke-width="1.6"/>
      </svg>
    </li>
    <li class="contacts__item">
      <span>www.facepage.example/quietharbourasia</span>
      <span class="contacts__square contacts__square--page"></span>
    </li>
    <li class="contacts__item">
      <span>www.quietharbourasia.ticketloom.example</span>
      <span class="contacts__square contacts__square--tickets"></span>
    </li>
  </ul>
</section>

</body>
</html>
```